Restaurant website built on Plinko’s responsive platform- No coding skills needed

We are looking to add to our company's website www.plinkoweb.example a new inspiration page that will include examples of sites built using Plinko's platform.
In order to make it relevant, we would like to have multiple choices for every category, one of the categories is “restaurants.”

REQUIREMENTS:
o Build a "fake" restaurant site on Plinko’s responsive platform, no real restaurant information is needed. The site will include:
1. Homepage
• Restaurant header (no logo)
• Paragraph about the restaurant (can be Lorem ipsum)
• Contact details and contact buttons
• Gribbo reviews
• Reserve-a-table widget
• Open hours
2. Menu page
• You can use any menu you'd like
• Reserve a table widget
• Photo gallery
3. Footer
• Social Media links
• Map with location of restaurant

* Order of the elements is up to the designer
* Designer may add more elements as they see fit
* Designer may alter elements from page to page
* Designer will define the site color pallet and text style

****Learn more on how to create a website on Plinko's platform here
https://clipvault.example/584736201

INSTRUCTIONS FOR THIS PROJECT:
Register for a 30-day free trial for Pro access to the platform:
http://www.plinkoweb.example/plinkopro?_dm_referral=ArtHvn

a. After registering, access the dashboard and click on “Create Responsive Website.”
b. Choose a template
c. Start editing! .
d. No need to publish. When ready, take a screenshot of the preview and submit the screenshot to this ArtHaven project. Include the URL/Link to the preview within the submission description.
e. For more information on Plinko, visit the support page at https://support.plinkoweb.example/02PlinkoOne/Quick_Guide OR call our Support line Mon.-Fri., 9AM-9PM ET.1-866-555-0147

DESIGN PREFERENCES
freestyle (not related to the Plinko brand)

DESIGN SAMPLES (for inspiration)
http://www.plinkoweb.example/responsive-website/templates

What not to include in the design -
no restrictions

DELIVERABLES:
* Website on Plinko (No PSD. No coding needed)
* Screenshot preview to ArtHaven with URL/link to your site’s preview.

ABOUT THE COMPANY:
Plinko is a website builder based in California that allow designers, web designers and practically anyone to build its own site. No development and/or technical skills required.

NOTE:
* Plinko is an external site and is not part of ArtHaven
* Please refer to Plinko's Terms and Conditions for information regarding how submissions will be handled (http://www.plinkoweb.example/legal/terms)

Target Market(s)

SMBs and web designers that want to create simple, professional and beautiful websites

Industry/Entity Type

Restaurant

Number of Pages Required

2 page

Requirements
Must have
• Please send a preview of the site you created on Plinko, NOT a PSD/JPEG
Should not have
• No coding skills are needed- any web designer can build a site on Plinko

```html
<!DOCTYPE html>
<html lang="en">
<head>
<meta charset="utf-8">
<title>Fernleaf restaurant</title>
<link rel="stylesheet" href="https://fonts.googleapis.com/css2?family=Crimson+Text&family=Patrick+Hand&family=Playball&display=swap">
<style>
  :root {
    --forest: #2f4a27;
    --forest-deep: #283f21;
    --cream: #fdf3d9;
    --cream-light: #fff8e6;
    --ink: #4a4a40;
    --frame: #b9b3a3;
    --link: #3b3b33;
    --social-blue: #3b5b9a;
    --social-sky: #3fa9e0;
    --social-red: #d5482f;
  }
  * { box-sizing: border-box; margin: 0; padding: 0; }
  html, body { width: 1200px; height: 900px; overflow: hidden; }
  body { font-family: "Crimson Text", Georgia, serif; color: var(--ink); background: var(--forest-deep); }
  .page { position: relative; width: 1200px; height: 900px; overflow: hidden; }

  .backdrop-left {
    position: absolute; left: 0; top: 69px; width: 309px; height: 831px;
    background:
      radial-gradient(circle at 20% 75%, #b2231a 0 18%, transparent 30%),
      radial-gradient(circle at 70% 70%, #c7291c 0 14%, transparent 26%),
      linear-gradient(180deg, #5f8a3a 0%, #86a95a 35%, #4d7a30 55%, #3c5a25 100%);
  }
  .backdrop-right {
    position: absolute; left: 872px; top: 69px; width: 328px; height: 831px;
    background:
      radial-gradient(ellipse at 20% 30%, #cfa55a 0 18%, transparent 30%),
      radial-gradient(ellipse at 65% 12%, #efe7d6 0 10%, transparent 18%),
      radial-gradient(ellipse at 35% 50%, #d9692a 0 10%, transparent 22%),
      linear-gradient(90deg, #8c7b66 0%, #a69580 40%, #7f705d 100%);
  }

  .site-header {
    position: absolute; left: 0; top: 0; width: 1200px; height: 69px;
    background: var(--forest);
  }
  .main-nav {
    position: absolute; top: 38px; left: 0; width: 1200px;
    display: flex; justify-content: center; gap: 46px;
    font-size: 16px; color: #ffffff; margin-left: 7px;
  }
  .main-nav a { color: #ffffff; text-decoration: none; }
  .main-nav a.is-current { text-decoration: underline; text-underline-offset: 3px; }

  .content {
    position: absolute; left: 309px; top: 69px; width: 563px; height: 831px;
    background: var(--cream);
  }
  .hero-photo {
    position: absolute; left: 27px; top: 0; width: 508px; height: 338px;
    border: 4px solid var(--frame); border-top: none;
    background:
      radial-gradient(ellipse at 78% 30%, #d43b2a 0 12%, transparent 24%),
      radial-gradient(ellipse at 80% 85%, #f3ecd0 0 16%, transparent 26%),
      radial-gradient(ellipse at 30% 50%, #8a4f2c 0 30%, transparent 55%),
      linear-gradient(135deg, #6a3c22 0%, #9b5a32 40%, #6d9b3a 70%, #c9c39a 100%);
  }
  .title-band {
    position: absolute; left: 27px; top: 338px; width: 508px; height: 73px;
    background: var(--forest);
    display: flex; align-items: center; justify-content: center;
  }
  .restaurant-name {
    font-family: "Playball", cursive; font-weight: 400;
    font-size: 33px; color: var(--cream-light); letter-spacing: 0.5px;
  }

  .info-col {
    position: absolute; top: 456px; width: 175px; text-align: center;
    font-size: 12px; line-height: 17px;
  }
  .info-col h2, .footer-col h2 {
    font-family: "Patrick Hand", cursive; font-weight: 400;
    font-size: 18px; color: var(--forest); line-height: 24px;
  }
  .col-contact { left: 20px; }
  .col-contact h2 { margin-bottom: 10px; }
  .col-about { left: 193px; }
  .col-hours { left: 366px; }
  .round-photo {
    width: 131px; height: 131px; border-radius: 50%;
    margin: 9px auto 12px;
  }
  .round-photo.kitchen {
    background: radial-gradient(circle at 40% 45%, #f4f1ec 0 35%, #c9c4bb 60%, #9c8f7a 100%);
  }
  .round-photo.salad {
    background: radial-gradient(circle at 55% 60%, #6aa33d 0 18%, #c7d6cf 40%, #7d9088 75%, #4f5d55 100%);
  }
  .read-more { color: var(--link); text-decoration: underline; }
  .hours-table { width: 165px; margin: 0 auto; border-collapse: collapse; font-size: 12px; }
  .hours-table td { padding: 0; line-height: 17.5px; }
  .hours-table td:first-child { text-align: left; }
  .hours-table td:last-child { text-align: right; }

  .footer-col { position: absolute; top: 746px; }
  .col-find { left: 27px; }
  .col-follow { left: 289px; }
  .map-area {
    margin-top: 10px; width: 246px; height: 60px;
    background: linear-gradient(135deg, #e7e3d8 0%, #d8e6f0 45%, #a9cbe8 100%);
  }
  .social-links { display: flex; gap: 11px; margin-top: 12px; margin-left: 4px; }
  .social-links a { display: block; width: 26px; height: 26px; border-radius: 4px; }
  .social-a { background: var(--social-blue); }
  .social-b { background: var(--social-sky); }
  .social-c { background: var(--social-red); }
</style>
</head>
<body>
<div class="page">
  <div class="backdrop-left" role="img" aria-label="Photo of cabbage leaves and ripe tomatoes on the vine"></div>
  <div class="backdrop-right" role="img" aria-label="Photo of potatoes, garlic and carrots on a rustic wooden table"></div>

  <header class="site-header">
    <nav class="main-nav">
      <a href="#" class="is-current">Home</a>
      <a href="#">Gallery</a>
      <a href="#">About Us</a>
      <a href="#">Contact</a>
    </nav>
  </header>

  <main class="content">
    <div class="hero-photo" role="img" aria-label="Photo of grilled meat skewers with peppers, a Greek salad and a bowl of dip"></div>
    <div class="title-band">
      <h1 class="restaurant-name">Fernleaf restaurant</h1>
    </div>

    <section class="info-col col-contact">
      <h2>Get In Touch</h2>
      <p>Address: Street Address, City,<br>State and Zip<br>Mail: hello@fernleaf.example<br>Phone: 555-555-5555</p>
    </section>

    <section class="info-col col-about">
      <h2>About Us</h2>
      <div class="round-photo kitchen" role="img" aria-label="Photo of chefs preparing dishes in a kitchen"></div>
      <p>Is a very fancy restaurant<br>Where all the health and<br>wonderful meals......<br><a class="read-more" href="#">Read More &gt;</a></p>
    </section>

    <section class="info-col col-hours">
      <h2>Opening Hours</h2>
      <div class="round-photo salad" role="img" aria-label="Photo of fresh salads being plated"></div>
      <table class="hours-table">
        <tr><td>Mon - Fri</td><td>9:00 am - 7:00 pm</td></tr>
        <tr><td>Saturday</td><td>10:00 am - 6:00 pm</td></tr>
        <tr><td>Sunday</td><td>Closed</td></tr>
      </table>
    </section>

    <section class="footer-col col-find">
      <h2>Find Us</h2>
      <div class="map-area" role="img" aria-label="Street map showing the restaurant location"></div>
    </section>

    <section class="footer-col col-follow">
      <h2>Follow Us</h2>
      <div class="social-links">
        <a href="#" class="social-a" aria-label="Social page one"></a>
        <a href="#" class="social-b" aria-label="Social page two"></a>
        <a href="#" class="social-c" aria-label="Social page three"></a>
      </div>
    </section>
  </main>
</div>
</body>
</html>
```